TIVRO

We provide order application for restaurants.
We need something modern, with a real visual identity.
it must be a landscape format.
Here our website: www.tivro.agency
a mix between those two leaflet would be great:
https://quelmart.brivodesk.com/share/ZtRwMnPq8L2x7bVyHc3d9/1
(landscape format)
https://app.nortelio.com/documents/4172906/view/518246097?accessId=3fa91d

IMPORTANT: this is not for taking. it's a leaflet to share by mail. (7 - 8 pages max)

Industry/Entity Type

web developement

Colors
6B429C
8869AF
B7A5CE
E3DAEB
F3F0F8

Requirements
Must have
• landscape format, to send by email (not for print).

```html
<!DOCTYPE html>
<html lang="fr">
<head>
<meta charset="utf-8">
<title>TIVRO – Dépliant application restaurant</title>
<link href="https://fonts.googleapis.com/css2?family=Bebas+Neue&family=Montserrat:wght@400;500;600;700&display=swap" rel="stylesheet">
<style>
  :root{
    --purple:#6B429C;
    --purple-mid:#8869AF;
    --lilac:#B7A5CE;
    --mist:#E3DAEB;
    --pale:#F3F0F8;
    --indigo:#4E3C9E;
    --title:#5A3E9E;
    --ink:#161616;
    --stage:#707070;
    --white:#ffffff;
  }
  *{margin:0;padding:0;box-sizing:border-box}
  html,body{width:1200px;height:1200px;overflow:hidden}
  body{background:var(--stage);font-family:"Montserrat",sans-serif;color:var(--ink);position:relative}
  .spread{position:absolute;left:271px;width:658px;height:512px;overflow:hidden;box-shadow:6px 8px 14px rgba(0,0,0,.35)}
  .spread--outside{top:62px}
  .spread--inside{top:625px}
  .sheet{position:absolute;left:0;top:0;width:1059px;height:824px;transform:scale(.6214);transform-origin:0 0}
  .sheet > svg.backdrop{position:absolute;left:0;top:0;width:1059px;height:824px}
  .abs{position:absolute}

  /* outside spread */
  .panel-title{font-size:26px;line-height:27px;color:var(--title);font-weight:700}
  .panel-title span{font-weight:500;display:block}
  .title-bar{height:4px;width:75px;background:var(--indigo)}
  .benefit{position:absolute;left:34px;width:290px}
  .benefit svg{position:absolute;left:0;top:2px;width:38px;height:38px}
  .benefit h3{margin-left:50px;font-size:15.5px;color:var(--title);font-weight:700}
  .benefit p{margin:8px 0 0 50px;font-size:11.3px;line-height:14px;text-align:justify;font-weight:500}

  .why{left:353px;width:353px;text-align:center}
  .why h2{font-size:26px;line-height:26px;color:var(--title);font-weight:700}
  .why h4{margin-top:16px;font-size:14px;font-weight:700}
  .why .rule{margin:10px auto 0;width:72px;height:3px;background:var(--indigo)}
  .why p{margin:16px auto 0;width:270px;font-size:11.4px;line-height:14.2px;font-weight:500}

  .brand{display:flex;align-items:center;gap:8px;color:var(--ink);font-weight:600;letter-spacing:1px}
  .brand i{display:block;background:var(--indigo)}
  .brand--small{font-size:24px}
  .brand--small i{width:28px;height:28px}
  .brand--large{font-size:40px}
  .brand--large i{width:42px;height:42px}

  .contact{left:353px;width:353px;text-align:center;color:var(--white)}
  .contact .ico{width:32px;height:32px;border-radius:6px;background:var(--white);margin:0 auto;display:flex;align-items:center;justify-content:center}
  .contact .ico svg{width:18px;height:18px}
  .contact .phone{font-size:22px;font-weight:600;letter-spacing:1px;margin:12px 0 18px}
  .contact .line{font-size:11.5px;margin:10px 0 18px}

  .cover-head{right:24px;top:530px;text-align:right;font-family:"Bebas Neue",sans-serif;font-size:51px;line-height:48px;color:var(--white)}
  .cover-sub{right:24px;top:680px;width:330px;text-align:right;font-size:14.2px;line-height:19px;font-weight:700;color:var(--mist)}
  .cover-btn{left:823px;top:758px;width:212px;height:28px;background:#1c1c1c;color:var(--white);font-size:14px;font-weight:700;display:flex;align-items:center;justify-content:center;letter-spacing:.5px}

  /* inside spread */
  .solution{left:35px;top:200px}
  .solution .bar{position:absolute;left:0;top:6px;width:5px;height:92px;background:var(--purple-mid)}
  .solution h2{margin-left:15px;font-size:30px;line-height:31px;color:var(--white);font-weight:700}
  .solution h2 span{font-weight:500;display:block}
  .solution p{margin-top:22px;width:212px;font-size:12.3px;line-height:15.5px;color:var(--white);font-weight:500}

  .service{position:absolute;width:290px}
  .service svg{position:absolute;left:0;top:-2px;width:30px;height:30px}
  .service h3{margin-left:45px;font-size:15px;color:var(--title);font-weight:700}
  .service p{margin:10px 0 0 45px;width:240px;font-size:11.3px;line-height:14px;text-align:justify;font-weight:500}

  .features-title{left:734px;top:230px;font-size:22px;line-height:28px;color:var(--white);font-weight:700}
  .features-bar{left:734px;top:290px;width:72px;height:4px;background:var(--white)}
  .feature{position:absolute;left:752px;width:280px;color:var(--white)}
  .feature svg{position:absolute;left:0;top:-4px;width:26px;height:26px}
  .feature h3{margin-left:37px;font-size:15px;font-weight:700}
  .feature p{margin:8px 0 0 37px;width:228px;font-size:11.3px;line-height:14px;text-align:justify;font-weight:500;color:var(--pale)}

  .device{position:absolute;border-radius:18px}
</style>
</head>
<body>

<!-- Outside spread -->
<section class="spread spread--outside">
  <div class="sheet">
    <svg class="backdrop" viewBox="0 0 1059 824" aria-hidden="true">
      <defs>
        <linearGradient id="foldLeft" x1="0" x2="1"><stop offset="0" stop-color="#ffffff"/><stop offset="1" stop-color="#e6e6ea"/></linearGradient>
        <linearGradient id="foldMid" x1="0" x2="1"><stop offset="0" stop-color="#ffffff"/><stop offset="1" stop-color="#ececf0"/></linearGradient>
        <linearGradient id="nightFade" x1="0" y1="0" x2="0" y2="1"><stop offset="0" stop-color="#3a3a3a"/><stop offset="1" stop-color="#0e0e0e"/></linearGradient>
        <linearGradient id="coverPurple" x1="0" y1="0" x2="1" y2="1"><stop offset="0" stop-color="#8C5FCB"/><stop offset="1" stop-color="#5E3D98"/></linearGradient>
      </defs>
      <rect x="0" y="0" width="353" height="824" fill="url(#foldLeft)"/>
      <rect x="353" y="0" width="353" height="824" fill="url(#foldMid)"/>
      <rect x="706" y="0" width="353" height="824" fill="#ffffff"/>
      <!-- top corner wedges -->
      <polygon points="270,0 353,0 353,62" fill="var(--indigo)"/>
      <polygon points="353,0 433,0 353,62" fill="var(--purple-mid)"/>
      <!-- panel 3 black stripe -->
      <polygon points="900,0 962,0 1059,88 1059,124" fill="#111"/>
    </svg>
    <!-- photo panel 1 -->
    <svg class="abs" style="left:0;top:0" width="1059" height="824" viewBox="0 0 1059 824" role="img" aria-label="Photo d'une serveuse souriante tenant une tablette dans un restaurant">
      <polygon points="0,340 353,555 353,824 0,824" fill="#8a6a4c"/>
      <polygon points="80,372 353,540 353,568 80,402" fill="var(--indigo)"/>
      <polygon points="200,480 353,575 353,600 200,505" fill="var(--purple-mid)"/>
      <!-- panel 2 night -->
      <polygon points="353,540 706,300 706,824 353,824" fill="url(#nightFade)"/>
      <polygon points="484,445 706,300 706,330 484,475" fill="var(--indigo)"/>
      <!-- panel 3 photo + purple -->
      <polygon points="706,330 1059,128 1059,824 706,824" fill="#6d4c33"/>
      <polygon points="706,300 812,228 812,258 706,330" fill="var(--indigo)"/>
      <polygon points="706,600 1059,390 1059,824 706,824" fill="url(#coverPurple)"/>
    </svg>

    <div class="abs" style="left:28px;top:32px">
      <h2 class="panel-title">La simplicité<span>à votre portée</span></h2>
      <div class="title-bar" style="margin-top:8px"></div>
    </div>

    <div class="benefit" style="top:120px">
      <svg viewBox="0 0 38 38" fill="none" stroke="var(--title)" stroke-width="1.6"><rect x="2" y="6" width="34" height="22" rx="2"/><rect x="7" y="11" width="10" height="7"/><line x1="20" y1="12" x2="31" y2="12"/><line x1="20" y1="17" x2="31" y2="17"/><line x1="19" y1="28" x2="19" y2="33"/><line x1="12" y1="33" x2="26" y2="33"/></svg>
      <h3>Ma propre application</h3>
      <p>Je m'équipe d'une application sur mesure. Votre logo, votre menu, votre restaurant!</p>
    </div>
    <div class="benefit" style="top:210px">
      <svg viewBox="0 0 38 38" fill="none" stroke="var(--title)" stroke-width="1.6"><path d="M34 4 C22 5 14 12 10 22 l6 6 C26 24 33 16 34 4z"/><circle cx="24" cy="14" r="3"/><path d="M10 22 l-6 2 4-8 6-1"/><path d="M16 28 l-2 6 8-4 1-6"/><path d="M8 30 l-4 4"/></svg>
      <h3>Mon chiffre d'affaires boosté</h3>
      <p>Mes commandes décollent grâce à un outil performant.</p>
    </div>
    <div class="benefit" style="top:289px">
      <svg viewBox="0 0 38 38" fill="none" stroke="var(--title)" stroke-width="1.6"><rect x="14" y="2" width="10" height="12"/><rect x="26" y="14" width="8" height="8" rx="2"/><circle cx="30" cy="28" r="4"/><path d="M4 30 l12-8 v14 z"/><line x1="17" y1="6" x2="21" y2="6"/><line x1="17" y1="10" x2="21" y2="10"/></svg>
      <h3>Mon coach marketing</h3>
      <p>Nos experts sont à vos côtés pour optimiser votre communication digitale.</p>
    </div>

    <div class="abs why" style="top:38px">
      <h2>Pourquoi<br>une App pour votre<br>restaurant ?</h2>
      <h4>UN CHIFFRE D'AFFAIRE DOUBLÉ !</h4>
      <div class="rule"></div>
      <p>Grâce à un taux de conversion client 3 fois supérieur au web, l'application mobile permet à nos restaurateurs partenaires de multiplier les commandes et d'augmenter la valeur du panier moyen. Votre application personnelle, la vitrine idéale pour booster votre activité !</p>
    </div>
    <div class="abs brand brand--small" style="left:460px;top:306px"><i></i>TIVRO</div>

    <div class="abs contact" style="top:530px">
      <div class="ico"><svg viewBox="0 0 24 24" fill="var(--indigo)"><path d="M6.6 10.8a15 15 0 0 0 6.6 6.6l2.2-2.2a1 1 0 0 1 1-.25 11.4 11.4 0 0 0 3.6.57 1 1 0 0 1 1 1V20a1 1 0 0 1-1 1A17 17 0 0 1 3 4a1 1 0 0 1 1-1h3.5a1 1 0 0 1 1 1c0 1.25.2 2.45.57 3.57a1 1 0 0 1-.25 1z"/></svg></div>
      <div class="phone">06-4170-5528</div>
      <div class="ico"><svg viewBox="0 0 24 24" fill="var(--indigo)"><path d="M3 5h18v14H3z M3 6l9 7 9-7" stroke="#fff" stroke-width="1.5"/></svg></div>
      <div class="line">contact@tivro.agency</div>
      <div class="ico"><svg viewBox="0 0 24 24" fill="none" stroke="var(--indigo)" stroke-width="1.8"><circle cx="12" cy="12" r="9"/><ellipse cx="12" cy="12" rx="4" ry="9"/><line x1="3" y1="12" x2="21" y2="12"/></svg></div>
      <div class="line">www.tivro.agency</div>
    </div>

    <div class="abs brand brand--large" style="left:760px;top:84px"><i></i>TIVRO</div>
    <div class="device" role="img" aria-label="Smartphone affichant la fiche d'une application de restaurant" style="left:896px;top:238px;width:128px;height:268px;background:linear-gradient(#2a2a2e,#0f0f12);border:5px solid #1a1a1a"></div>
    <div class="abs cover-head">ENSEMBLE<br>CREEONS VOTRE<br>APPLICATION</div>
    <div class="abs cover-sub">VOS CLIENTS RECHERCHENT VOTRE APPLICATION SUR L'APPHUB OU LE PLAYMART</div>
    <div class="abs cover-btn">WWW.TIVRO.AGENCY</div>
  </div>
</section>

<!-- Inside spread -->
<section class="spread spread--inside">
  <div class="sheet">
    <svg class="backdrop" viewBox="0 0 1059 824" aria-hidden="true">
      <defs>
        <linearGradient id="paperL" x1="0" x2="1"><stop offset="0" stop-color="#ffffff"/><stop offset="1" stop-color="#e8e8ec"/></linearGradient>
        <linearGradient id="paperM" x1="0" x2="1"><stop offset="0" stop-color="#ffffff"/><stop offset="1" stop-color="#ececf0"/></linearGradient>
        <linearGradient id="darkWedge" x1="0" y1="0" x2="1" y2="0"><stop offset="0" stop-color="#111"/><stop offset="1" stop-color="#2b2b2b"/></linearGradient>
        <linearGradient id="featPurple" x1="0" y1="0" x2="0" y2="1"><stop offset="0" stop-color="#5A4AA8"/><stop offset="1" stop-color="#8759C0"/></linearGradient>
      </defs>
      <rect x="0" y="0" width="353" height="824" fill="url(#paperL)"/>
      <rect x="353" y="0" width="353" height="824" fill="url(#paperM)"/>
    </svg>
    <svg class="abs" style="left:0;top:0" width="1059" height="824" viewBox="0 0 1059 824" role="img" aria-label="Photo d'une salle de restaurant éclairée teintée violet et d'un bol de salade aux œufs">
      <polygon points="0,0 706,0 706,80 353,305 0,110" fill="#6b4f9a"/>
      <polygon points="0,0 706,0 706,80 353,305 0,110" fill="#3e2f6e" opacity=".35"/>
      <polygon points="706,0 1059,0 1059,310 706,110" fill="#b7a089"/>
      <polygon points="0,118 360,310 0,520" fill="url(#darkWedge)"/>
      <polygon points="0,520 360,310 430,270 0,560" fill="#1b1b1b"/>
      <polygon points="0,545 275,372 275,410 0,585" fill="var(--indigo)"/>
      <polygon points="706,110 1059,310 1059,824 706,824" fill="url(#featPurple)"/>
    </svg>

    <div class="abs solution">
      <div class="bar"></div>
      <h2>Une<br>Solution<span>clé en main</span></h2>
      <p>Lancer l'application de VOTRE restaurant dans les meilleures conditions. TIVRO met à votre disposition un pack de lancement complet pour un succès assuré.</p>
    </div>

    <div class="service" style="left:45px;top:575px">
      <svg viewBox="0 0 30 30" fill="none" stroke="var(--title)" stroke-width="2"><rect x="8" y="2" width="14" height="26" rx="2"/><line x1="13" y1="24" x2="17" y2="24"/></svg>
      <h3>APPLICATION MOBILE</h3>
      <p>Votre application mobile disponible sur l'Droidix PlayMart et l'AppHub</p>
    </div>
    <div class="service" style="left:45px;top:686px">
      <svg viewBox="0 0 30 30" fill="var(--title)"><path d="M11 4a3 3 0 0 1 6 0v10l6 1a3 3 0 0 1 2.5 3.5L24 27H11l-5-8 2-2 3 3z"/></svg>
      <h3>ADMIN PANEL</h3>
      <p>Une tablette avec une interface intuitive pour piloter votre application (mise à jour de l'offre, mise en place d'action commerciale, envoi de notification push, suivi des statistiques ...)</p>
    </div>

    <div class="device" role="img" aria-label="Smartphone blanc affichant un menu de sushis" style="left:540px;top:42px;width:132px;height:280px;background:linear-gradient(#f4f4f6,#d9d9de);border:2px solid #bbb"></div>

    <div class="service" style="left:385px;top:345px">
      <svg viewBox="0 0 30 30" fill="none" stroke="var(--title)" stroke-width="2"><rect x="2" y="4" width="26" height="18" rx="1"/><path d="M12 9 l7 4-7 4z" fill="var(--title)"/><line x1="9" y1="27" x2="21" y2="27"/></svg>
      <h3>FORMATION</h3>
      <p>Formation de lancement et tutoriels vidéo pour maîtriser votre interface</p>
    </div>
    <div class="service" style="left:385px;top:457px">
      <svg viewBox="0 0 30 30" fill="var(--title)"><path d="M4 2 L28 15 L4 28 z"/></svg>
      <h3>STICKERS</h3>
      <p>Sticker de l'AppHub et du PlayMart à coller sur la vitrine de votre commerce</p>
    </div>
    <div class="service" style="left:385px;top:572px">
      <svg viewBox="0 0 30 30" fill="var(--title)"><path d="M3 11h6l14-7v22L9 19H3z"/><rect x="8" y="19" width="4" height="8"/></svg>
      <h3>DIGITAL MARKETING</h3>
      <p>Création graphique de trois posts sur vos réseaux sociaux et d'une video de teasing (25 sec) pour promouvoir votre application</p>
    </div>
    <div class="service" style="left:385px;top:713px">
      <svg viewBox="0 0 30 30" fill="none" stroke="var(--title)" stroke-width="2"><path d="M2 8V2h6M22 2h6v6M28 22v6h-6M8 28H2v-6"/><rect x="8" y="8" width="6" height="6"/><rect x="16" y="16" width="6" height="6"/></svg>
      <h3>FLYER</h3>
      <p>Création de 500 flyers personnalisés avec l'intégration du QR code pour un téléchargement direct de l'application.</p>
    </div>

    <div class="abs features-title">Découvrez<br>vos fonctionnalités</div>
    <div class="abs features-bar"></div>

    <div class="feature" style="top:325px">
      <svg viewBox="0 0 26 26" fill="none" stroke="#fff" stroke-width="1.8"><path d="M3 4h3l3 12h10l3-8H8"/><circle cx="10" cy="21" r="2"/><circle cx="18" cy="21" r="2"/></svg>
      <h3>Une livraison maitrisée</h3>
      <p>Définissez un montant de commande minimum par secteur.</p>
    </div>
    <div class="feature" style="top:402px">
      <svg viewBox="0 0 26 26" fill="#fff"><rect x="3" y="14" width="4" height="9"/><rect x="10" y="9" width="4" height="14"/><rect x="17" y="4" width="4" height="19"/></svg>
      <h3>Statistiques</h3>
      <p>Analysez vos commandes et adaptez votre offre.</p>
    </div>
    <div class="feature" style="top:477px">
      <svg viewBox="0 0 26 26" fill="none" stroke="#fff" stroke-width="1.8"><rect x="4" y="9" width="18" height="14"/><path d="M9 9V6a4 4 0 0 1 8 0v3"/></svg>
      <h3>Facilitez l'achat</h3>
      <p>Un processus de commande simplifié grâce aux moyens de paiements enregistrés.</p>
    </div>
    <div class="feature" style="top:566px">
      <svg viewBox="0 0 26 26" fill="#fff"><circle cx="13" cy="8" r="3"/><circle cx="5" cy="11" r="2.5"/><circle cx="21" cy="11" r="2.5"/><path d="M7 22a6 6 0 0 1 12 0z"/><path d="M1 22a4 4 0 0 1 6-3v3z"/><path d="M25 22a4 4 0 0 0-6-3v3z"/></svg>
      <h3>Expérience utilisateur</h3>
      <p>Une navigation ergonomique et intuitive pensée pour le mobile.</p>
    </div>
    <div class="feature" style="top:641px">
      <svg viewBox="0 0 26 26" fill="none" stroke="#fff" stroke-width="1.8"><circle cx="17" cy="6" r="3" fill="#fff"/><path d="M2 14h5l5 4h8l3-3"/><path d="M2 20h6l4 2"/></svg>
      <h3>Démarquez-vous</h3>
      <p>Distancez vos concurrents grâce à un outil numérique innovant.</p>
    </div>
    <div class="feature" style="top:720px">
      <svg viewBox="0 0 26 26" fill="#fff"><path d="M10 4a2.5 2.5 0 0 1 5 0v8l5 1a2.5 2.5 0 0 1 2 3l-1.5 8H10l-4-7 2-2 2 2z"/></svg>
      <h3>Click &amp; Collect</h3>
      <p>Vos clients choisissent la livraison ou le Click &amp; Collect.</p>
    </div>
  </div>
</section>

</body>
</html>
```